Banner Ad for Resume Writers

This ad is for www.tallowcareerpages.com.au

The site offers a resume writing service in Australia. Take a look at the site for more info.

Colours to use: Blue, orange, yellow or whatever works.

Image specifications:
Pixel size: 160w X 600h (Skyscraper)
Image format: GIF (25K max)
Must have a border and must not use transparent backgrounds

Text can include:

'Professional Resume Writers'

and

'Is your resume good enough? Ask the Experts!'

The text 'Free resume health check' could be included but the banner should look good even if this text is not included as it may need to be removed.

Target Market(s)

Job seekers

Industry/Entity Type

Health

Nice to have
• It would be good to include an attractive smiling face making eye contact with the viewer.
Should not have
• Should not be too busy. Avoid clutter.

```html
<!DOCTYPE html>
<html lang="en">
<head>
<meta charset="utf-8">
<title>Professional Resume Writers – Skyscraper Banners</title>
<link rel="stylesheet" href="https://fonts.googleapis.com/css2?family=Arvo:wght@400;700&family=Roboto+Slab:wght@300;400&family=Oswald:wght@600&family=Arimo:wght@700&display=swap">
<style>
  :root {
    --canvas: #ffffff;
    --ink: #000000;
    --white: #ffffff;
    --accent-blue: #19b3ea;
    --tagline-grey: #8a8a8a;
    --button-top: #f2434a;
    --button-bottom: #b80d12;
    --hair: #d68f45;
    --hair-light: #e9b06a;
    --skin: #f2c6b6;
    --skin-deep: #e9a99a;
    --frame: #333333;
  }

  * { box-sizing: border-box; margin: 0; padding: 0; }

  html, body {
    width: 1200px;
    height: 800px;
    overflow: hidden;
    background: var(--canvas);
  }

  .sheet {
    position: relative;
    width: 1200px;
    height: 800px;
  }

  .banner {
    position: absolute;
    top: 95px;
    width: 160px;
    height: 599px;
    border: 1px solid var(--frame);
    overflow: hidden;
    background: var(--skin);
  }
  .banner--1 { left: 15px; }
  .banner--2 { left: 214px; }
  .banner--3 { left: 413px; }
  .banner--4 { left: 612px; }
  .banner--5 { left: 811px; }
  .banner--6 { left: 1010px; }

  .portrait {
    position: absolute;
    left: 0; top: 0;
    width: 100%;
    height: 100%;
    background: linear-gradient(180deg,
      var(--hair) 0%, var(--hair-light) 18%, var(--hair) 30%,
      var(--skin-deep) 38%, var(--skin) 50%, var(--skin) 100%);
  }

  .masthead {
    position: absolute;
    left: 0; top: 10px;
    width: 100%;
    height: 56px;
    background: linear-gradient(180deg, #000 0%, #000 85%, rgba(0,0,0,0.6) 100%);
    color: var(--white);
    text-align: center;
    font-family: "Roboto Slab", serif;
    font-weight: 300;
  }
  .masthead__title {
    display: block;
    font-size: 22px;
    line-height: 26px;
    padding-top: 2px;
  }
  .masthead__subtitle {
    display: block;
    font-size: 16.5px;
    line-height: 20px;
  }

  .pitch {
    position: absolute;
    left: 0;
    width: 100%;
    background: var(--ink);
    color: var(--white);
    text-align: center;
  }
  .banner--short .pitch { top: 384px; height: 186px; }
  .banner--tall .pitch { top: 370px; height: 229px; }

  .pitch__line {
    position: absolute;
    left: 0;
    width: 100%;
    font-family: "Arvo", serif;
    font-weight: 700;
    white-space: nowrap;
  }
  .pitch__intro { font-size: 25px; line-height: 30px; }
  .pitch__keyword { font-size: 27px; line-height: 30px; letter-spacing: 0.5px; }
  .pitch__industry { color: var(--accent-blue); font-family: "Arimo", sans-serif; line-height: 30px; }
  .pitch__industry--large { font-size: 27px; }
  .pitch__industry--code { font-size: 29px; font-family: "Arvo", serif; }
  .pitch__industry--small { font-size: 19.5px; }
  .pitch__question { font-size: 18.5px; line-height: 24px; }

  .tagline {
    position: absolute;
    left: 0;
    width: 100%;
    font-family: "Arimo", sans-serif;
    font-weight: 700;
    font-size: 14.5px;
    line-height: 18px;
    color: var(--tagline-grey);
  }

  .cta {
    position: absolute;
    left: 12px;
    width: 134px;
    height: 29px;
    border-radius: 3px;
    background: linear-gradient(180deg, var(--button-top) 0%, #e0232a 48%, var(--button-bottom) 52%, #d01c22 100%);
    color: var(--white);
    font-family: "Oswald", sans-serif;
    font-weight: 600;
    font-size: 16px;
    line-height: 29px;
    text-align: center;
    letter-spacing: 0.2px;
  }

  /* short panel rows */
  .banner--short .row-intro { top: 10px; }
  .banner--short .row-keyword { top: 44px; }
  .banner--short .row-question { top: 76px; }
  .banner--short .tagline { top: 116px; }
  .banner--short .cta { top: 142px; }

  /* tall panel rows */
  .banner--tall .row-intro { top: 10px; }
  .banner--tall .row-industry { top: 45px; }
  .banner--tall .row-keyword { top: 82px; }
  .banner--tall .row-question { top: 113px; }
  .banner--tall .tagline { top: 152px; }
  .banner--tall .cta { top: 178px; }
</style>
</head>
<body>
<main class="sheet">

  <section class="banner banner--1 banner--short">
    <div class="portrait" role="img" aria-label="Close-up photo of a woman's face with red hair and blue eye"></div>
    <header class="masthead"><span class="masthead__title">Professional</span><span class="masthead__subtitle">Resume Writers</span></header>
    <div class="pitch">
      <span class="pitch__line pitch__intro row-intro">Is your</span>
      <span class="pitch__line pitch__keyword row-keyword">RESUME</span>
      <span class="pitch__line pitch__question row-question">good enough?</span>
      <span class="tagline">Ask the Experts!</span>
      <span class="cta">CLICK HERE</span>
    </div>
  </section>

  <section class="banner banner--2 banner--short">
    <div class="portrait" role="img" aria-label="Close-up photo of a woman's face with red hair and blue eye"></div>
    <header class="masthead"><span class="masthead__title">Professional</span><span class="masthead__subtitle">Resume Writers</span></header>
    <div class="pitch">
      <span class="pitch__line pitch__intro row-intro">Is your</span>
      <span class="pitch__line pitch__keyword row-keyword">RESUME</span>
      <span class="pitch__line pitch__question row-question">good enough?</span>
      <span class="tagline">Get Started Now!</span>
      <span class="cta">CLICK HERE</span>
    </div>
  </section>

  <section class="banner banner--3 banner--tall">
    <div class="portrait" role="img" aria-label="Close-up photo of a woman's face with red hair and blue eye"></div>
    <header class="masthead"><span class="masthead__title">Professional</span><span class="masthead__subtitle">Resume Writers</span></header>
    <div class="pitch">
      <span class="pitch__line pitch__intro row-intro">Is your</span>
      <span class="pitch__line pitch__industry pitch__industry--large row-industry">mining</span>
      <span class="pitch__line pitch__keyword row-keyword">RESUME</span>
      <span class="pitch__line pitch__question row-question">good enough?</span>
      <span class="tagline">Get Started Now!</span>
      <span class="cta">CLICK HERE</span>
    </div>
  </section>

  <section class="banner banner--4 banner--tall">
    <div class="portrait" role="img" aria-label="Close-up photo of a woman's face with red hair and blue eye"></div>
    <header class="masthead"><span class="masthead__title">Professional</span><span class="masthead__subtitle">Resume Writers</span></header>
    <div class="pitch">
      <span class="pitch__line pitch__intro row-intro">Is your</span>
      <span class="pitch__line pitch__industry pitch__industry--code row-industry">FIFO</span>
      <span class="pitch__line pitch__keyword row-keyword">RESUME</span>
      <span class="pitch__line pitch__question row-question">good enough?</span>
      <span class="tagline">Get Started Now!</span>
      <span class="cta">CLICK HERE</span>
    </div>
  </section>

  <section class="banner banner--5 banner--tall">
    <div class="portrait" role="img" aria-label="Close-up photo of a woman's face with red hair and blue eye"></div>
    <header class="masthead"><span class="masthead__title">Professional</span><span class="masthead__subtitle">Resume Writers</span></header>
    <div class="pitch">
      <span class="pitch__line pitch__intro row-intro">Is your</span>
      <span class="pitch__line pitch__industry pitch__industry--small row-industry">engineering</span>
      <span class="pitch__line pitch__keyword row-keyword">RESUME</span>
      <span class="pitch__line pitch__question row-question">good enough?</span>
      <span class="tagline">Ask the Experts!</span>
      <span class="cta">CLICK HERE</span>
    </div>
  </section>

  <section class="banner banner--6 banner--tall">
    <div class="portrait" role="img" aria-label="Close-up photo of a woman's face with red hair and blue eye"></div>
    <header class="masthead"><span class="masthead__title">Professional</span><span class="masthead__subtitle">Resume Writers</span></header>
    <div class="pitch">
      <span class="pitch__line pitch__intro row-intro">Is your</span>
      <span class="pitch__line pitch__industry pitch__industry--small row-industry">accounting</span>
      <span class="pitch__line pitch__keyword row-keyword">RESUME</span>
      <span class="pitch__line pitch__question row-question">good enough?</span>
      <span class="tagline">Ask the Experts!</span>
      <span class="cta">CLICK HERE</span>
    </div>
  </section>

</main>
</body>
</html>
```